Baby Led Weaning App complete design

I want to develop a new app and I need full design for it, including screens, toolbars, icons, images, logo,etc.
The app is aiming to show the User information about baby led weaning, with theory and guidelines and it should also contain a section with recipes for baby lead weaning.

Industry/Entity Type
Baby
Requirements
Must have
- Full design for the app, including screens, toolbars, icons, images, logo,etc.
- The app will be used on smartphones and tablets so design should consider different screen sizes.

Nice to have
- The app is mainly for mums with babys. The design should be bright, happy (positive) and easy to use.
- It would be good to have nice images of babys feeding themselves (no bottle milk). The images in the documents provided need to be replaced.
- Colurs should be gender neutral (not specific to girl or boy).

Should not have
- The should not look too serious or cold.
- Nothing that can be interpreted as negative, heavy, complicated or sad.

```html
<!DOCTYPE html>
<html lang="en">
<head>
<meta charset="utf-8">
<title>Recipes – Popular</title>
<link href="https://fonts.googleapis.com/css2?family=Roboto:wght@400;500;700&display=swap" rel="stylesheet">
<style>
  :root{
    --page-bg:#d6e4f0;
    --brand:#7b0f5e;
    --white:#ffffff;
    --list-bg:#eef0f3;
    --text-dark:#2b2b2b;
    --text-body:#6f6f6f;
    --text-meta:#8d8d8d;
    --tab-idle:#6a6a6a;
    --star-on:#f0b323;
    --star-off:#c9c9c9;
    --advert:#e8611a;
    --card-shadow:rgba(0,0,0,.07);
  }
  *{box-sizing:border-box;margin:0;padding:0}
  html,body{width:1200px;height:1200px;overflow:hidden}
  body{background:var(--page-bg);font-family:"Roboto",Helvetica,Arial,sans-serif;position:relative}

  .screen{position:absolute;left:280px;top:28px;width:640px;height:1143px;background:var(--white);overflow:hidden;display:flex;flex-direction:column}

  .status-bar{height:49px;background:var(--brand);color:var(--white);display:flex;align-items:center;justify-content:space-between;padding:0 9px 0 8px;font-size:18px}
  .status-left,.status-right{display:flex;align-items:center;gap:6px;width:200px}
  .status-right{justify-content:flex-end}
  .signal{display:flex;gap:2px}
  .signal i{width:9px;height:9px;border-radius:50%;border:1.3px solid var(--white);display:block}
  .signal i.on{background:var(--white)}
  .battery{width:38px;height:16px;border:1.5px solid var(--white);border-radius:3px;padding:1.5px;position:relative}
  .battery::before{content:"";display:block;width:100%;height:100%;background:var(--white);border-radius:1px}
  .battery::after{content:"";position:absolute;right:-5px;top:4px;width:3px;height:6px;background:var(--white);border-radius:0 2px 2px 0}

  .app-bar{height:66px;background:var(--brand);display:flex;align-items:center;justify-content:space-between;padding:0 14px 0 20px;color:var(--white)}
  .app-mark{width:44px;height:44px;border-radius:50%;background:#f5c842}
  .app-title{font-size:27px;font-weight:700;letter-spacing:.5px}
  .menu-dots{display:flex;flex-direction:column;gap:5px;width:44px;align-items:flex-end;padding-right:6px}
  .menu-dots i{width:5px;height:5px;border-radius:50%;background:var(--white);display:block}

  .tabs{height:59px;display:flex;background:var(--white);position:relative;border-bottom:1px solid #e2e2e2}
  .tab{flex:1;display:flex;align-items:center;justify-content:center;font-size:22px;font-weight:500;color:var(--tab-idle);letter-spacing:.3px}
  .tab.active{color:var(--brand);border-bottom:3px solid var(--brand)}

  .recipe-list{flex:1;background:var(--list-bg);overflow:hidden;padding:15px 16px 0}
  .recipe-card{height:173px;background:var(--white);margin-bottom:13px;display:flex;padding:9px;box-shadow:0 1px 2px var(--card-shadow)}
  .recipe-photo{width:163px;height:154px;flex:none}
  .recipe-info{padding-left:21px;display:flex;flex-direction:column;min-width:0}
  .recipe-title{font-size:22px;color:var(--text-dark);white-space:nowrap;margin-top:4px;line-height:1.2}
  .rating{display:flex;align-items:center;gap:4px;margin-top:7px;font-size:15px;color:var(--text-meta)}
  .rating svg{width:16px;height:16px}
  .rating .count{margin-left:6px}
  .recipe-desc{font-size:16.5px;line-height:22px;color:var(--text-body);margin-top:10px}
  .recipe-meta{display:flex;gap:30px;margin-top:12px;font-size:15px;color:var(--text-meta)}
  .meta-item{display:flex;align-items:center;gap:10px}
  .meta-item svg{width:18px;height:18px;fill:none;stroke:var(--text-meta);stroke-width:1.4}

  .photo-fish{background:radial-gradient(circle at 55% 50%,#d9a24a 0 28%,#f1ece2 29% 58%,#d8cfc2 60%)}
  .photo-meatballs{background:radial-gradient(circle at 50% 50%,#9a6440 0 45%,#5d8e86 70%)}
  .photo-cauliflower{background:linear-gradient(135deg,#e9d7ae 0%,#d9bd86 50%,#f2efe8 100%)}
  .photo-chicken{background:radial-gradient(circle at 55% 45%,#d0481e 0 45%,#f2f0ec 62%,#8b2d1a 80%)}
  .photo-fritter{background:radial-gradient(circle at 50% 50%,#e2bb62 0 28%,#f4f1ea 30% 65%,#7fc9cf 90%)}

  .advert-bar{height:85px;flex:none;background:var(--white);display:flex;align-items:center;justify-content:center;color:var(--advert);font-size:28px;letter-spacing:.5px}
</style>
</head>
<body>
<svg width="0" height="0" style="position:absolute">
  <defs>
    <symbol id="star" viewBox="0 0 24 24"><path d="M12 2l2.9 6.6 7.1.7-5.4 4.8 1.6 7-6.2-3.7-6.2 3.7 1.6-7L2 9.3l7.1-.7z"/></symbol>
    <symbol id="clock" viewBox="0 0 20 20"><circle cx="10" cy="10" r="8"/><path d="M10 5v5l3 2"/></symbol>
    <symbol id="hat" viewBox="0 0 20 20"><path d="M5 12c-2.5 0-3.5-4-1-5 .5-3 4-4 6-2 2-2 5.5-1 6 2 2.5 1 1.5 5-1 5v4H5z"/><path d="M5 14h10"/></symbol>
    <symbol id="heart" viewBox="0 0 20 20"><path d="M10 17S2 12 2 7a4 4 0 0 1 8-1 4 4 0 0 1 8 1c0 5-8 10-8 10z"/></symbol>
  </defs>
</svg>

<main class="screen">
  <div class="status-bar">
    <div class="status-left">
      <span class="signal"><i class="on"></i><i class="on"></i><i class="on"></i><i></i><i></i></span>
      <span>NOVA</span>
      <svg width="18" height="14" viewBox="0 0 18 14" fill="none" stroke="#fff" stroke-width="2"><path d="M1 5a11 11 0 0 1 16 0M4 8a6.5 6.5 0 0 1 10 0"/><circle cx="9" cy="11.5" r="1.5" fill="#fff" stroke="none"/></svg>
    </div>
    <span class="time">4:21 PM</span>
    <div class="status-right"><span>100%</span><span class="battery"></span></div>
  </div>

  <header class="app-bar">
    <span class="app-mark"></span>
    <h1 class="app-title">RECIPES</h1>
    <span class="menu-dots"><i></i><i></i><i></i></span>
  </header>

  <nav class="tabs">
    <div class="tab active">POPULAR</div>
    <div class="tab">EXPLORE</div>
  </nav>

  <section class="recipe-list">
    <article class="recipe-card">
      <div class="recipe-photo photo-fish" role="img" aria-label="Golden fish pie bites on a white plate"></div>
      <div class="recipe-info">
        <h2 class="recipe-title">Weaning recipe: Fish pie bites</h2>
        <div class="rating">
          <svg fill="var(--star-on)"><use href="#star"/></svg><svg fill="var(--star-on)"><use href="#star"/></svg><svg fill="var(--star-on)"><use href="#star"/></svg><svg fill="var(--star-on)"><use href="#star"/></svg><svg fill="var(--star-on)"><use href="#star"/></svg>
          <span class="count">(3 ratings)</span>
        </div>
        <p class="recipe-desc">Lorem ipsum dolor sit amet, consectetur adipiscing elit. Etiam vitae eros efficitur, finibus sapien et ...</p>
        <div class="recipe-meta">
          <span class="meta-item"><svg><use href="#clock"/></svg>2 Hours and 5 Mins</span>
          <span class="meta-item"><svg><use href="#hat"/></svg>Easy</span>
        </div>
      </div>
    </article>

    <article class="recipe-card">
      <div class="recipe-photo photo-meatballs" role="img" aria-label="Chicken meatballs in a teal bowl"></div>
      <div class="recipe-info">
        <h2 class="recipe-title">Weaning recipe: Chicken meatballs</h2>
        <div class="rating">
          <svg fill="var(--star-on)"><use href="#star"/></svg><svg fill="var(--star-on)"><use href="#star"/></svg><svg fill="var(--star-on)"><use href="#star"/></svg><svg fill="var(--star-on)"><use href="#star"/></svg><svg fill="var(--star-on)"><use href="#star"/></svg>
          <span class="count">(3 ratings)</span>
        </div>
        <p class="recipe-desc">Lorem ipsum dolor sit amet, consectetur adipiscing elit. Etiam vitae eros efficitur, finibus sapien et ...</p>
        <div class="recipe-meta">
          <span class="meta-item"><svg><use href="#clock"/></svg>2 Hours and 5 Mins</span>
          <span class="meta-item"><svg><use href="#hat"/></svg>Easy</span>
          <span class="meta-item"><svg><use href="#heart"/></svg>Healthy</span>
        </div>
      </div>
    </article>

    <article class="recipe-card">
      <div class="recipe-photo photo-cauliflower" role="img" aria-label="Cauliflower cheese cakes with vegetables and dip"></div>
      <div class="recipe-info">
        <h2 class="recipe-title">Toddler recipe: Cauliflower cheese ca ...</h2>
        <div class="rating">
          <svg fill="var(--star-on)"><use href="#star"/></svg><svg fill="var(--star-on)"><use href="#star"/></svg><svg fill="var(--star-on)"><use href="#star"/></svg><svg fill="var(--star-on)"><use href="#star"/></svg><svg fill="var(--star-off)"><use href="#star"/></svg>
          <span class="count">(1 rating)</span>
        </div>
        <p class="recipe-desc">Lorem ipsum dolor sit amet, consectetur adipiscing elit. Etiam vitae eros efficitur, finibus sapien et ...</p>
        <div class="recipe-meta">
          <span class="meta-item"><svg><use href="#clock"/></svg>2 Hours and 5 Mins</span>
          <span class="meta-item"><svg><use href="#hat"/></svg>Easy</span>
          <span class="meta-item"><svg><use href="#heart"/></svg>Healthy</span>
        </div>
      </div>
    </article>

    <article class="recipe-card">
      <div class="recipe-photo photo-chicken" role="img" aria-label="Glazed sweet chilli chicken in a white bowl"></div>
      <div class="recipe-info">
        <h2 class="recipe-title">Lorem ipsum dolor sit adipiscing elit.</h2>
        <div class="rating">
          <svg fill="var(--star-on)"><use href="#star"/></svg><svg fill="var(--star-on)"><use href="#star"/></svg><svg fill="var(--star-on)"><use href="#star"/></svg><svg fill="var(--star-on)"><use href="#star"/></svg><svg fill="var(--star-off)"><use href="#star"/></svg>
          <span class="count">(3 ratings)</span>
        </div>
        <p class="recipe-desc">Lorem ipsum dolor sit amet, consectetur adipiscing elit. Etiam vitae eros efficitur, finibus sapien et ...</p>
        <div class="recipe-meta">
          <span class="meta-item"><svg><use href="#clock"/></svg>2 Hours and 5 Mins</span>
          <span class="meta-item"><svg><use href="#hat"/></svg>Easy</span>
          <span class="meta-item"><svg><use href="#heart"/></svg>Healthy</span>
        </div>
      </div>
    </article>

    <article class="recipe-card">
      <div class="recipe-photo photo-fritter" role="img" aria-label="Fritter topped with cream and herbs on a plate"></div>
      <div class="recipe-info">
        <h2 class="recipe-title">Lorem ipsum dolor sit adipiscing elit.</h2>
        <div class="rating">
          <svg fill="var(--star-on)"><use href="#star"/></svg><svg fill="var(--star-on)"><use href="#star"/></svg><svg fill="var(--star-on)"><use href="#star"/></svg><svg fill="var(--star-on)"><use href="#star"/></svg><svg fill="var(--star-off)"><use href="#star"/></svg>
          <span class="count">(3 ratings)</span>
        </div>
        <p class="recipe-desc">Lorem ipsum dolor sit amet, consectetur adipiscing elit. Etiam vitae eros efficitur, finibus sapien et ...</p>
      </div>
    </article>
  </section>

  <footer class="advert-bar">ADVERT</footer>
</main>
</body>
</html>
```